Classic Minimalistic Business Card

Design a classic, minimalistic Business Card. Please find inspiration in the attached Classic Minimalistic examples. My information:
Name: Glen Ovamir
Company: Ovamir Capital
Logo: OC
Address: 1470 N Thornwick Rd, Suite 210 | Marlow Falls, ST 00412
Phone: 555-555-0192
Email: glenovamir@pvt.example
Slogan: Building Strength Through Capital

Feel free to leave out any of the information above except my name.

I have selected Double-sided, but I am also open to Single-sided

Target Market(s)

22-70. income greater than 150k/year

Industry/Entity Type

Finance

Contact Information for Business Card

See Project Description

Requirements
Must have
• Ivory or "antiqued" background similar to the reference pictures

```html
<!DOCTYPE html>
<html lang="en">
<head>
<meta charset="utf-8">
<title>Ovamir Capital – Business Card</title>
<link rel="stylesheet" href="https://fonts.googleapis.com/css2?family=Arvo:ital,wght@0,400;0,700;1,400&display=swap">
<style>
  :root {
    --backdrop: #efeeec;
    --card-kraft: #8f7758;
    --card-kraft-light: #977f60;
    --ink: #382f26;
    --ink-soft: #43392e;
  }
  * { margin: 0; padding: 0; box-sizing: border-box; }
  html, body {
    width: 1200px;
    height: 798px;
    overflow: hidden;
    background: var(--backdrop);
  }
  .canvas {
    position: relative;
    width: 1200px;
    height: 798px;
  }
  .business-card {
    position: absolute;
    left: 60px;
    top: 100px;
    width: 1080px;
    height: 598px;
    background: radial-gradient(ellipse at 40% 40%, var(--card-kraft-light), var(--card-kraft));
    color: var(--ink);
    font-family: "Arvo", Georgia, serif;
  }
  .holder-name {
    position: absolute;
    left: 54px;
    top: 56px;
    font-size: 41px;
    font-weight: 400;
    letter-spacing: 0.3px;
  }
  .brand-block {
    position: absolute;
    left: 0;
    right: 0;
    top: 240px;
    text-align: center;
  }
  .brand-name {
    font-size: 58px;
    font-weight: 400;
    letter-spacing: 2px;
    line-height: 1;
    color: var(--ink);
  }
  .brand-slogan {
    margin-top: 16px;
    font-size: 24px;
    font-style: italic;
    color: var(--ink-soft);
  }
  .contact-block {
    position: absolute;
    left: 0;
    right: 0;
    top: 478px;
    text-align: center;
    font-size: 27px;
    line-height: 42px;
    color: var(--ink-soft);
    letter-spacing: 0.3px;
  }
  .divider { margin: 0 10px; }
</style>
</head>
<body>
<div class="canvas">
  <section class="business-card">
    <h1 class="holder-name">Glen Ovamir</h1>
    <div class="brand-block">
      <div class="brand-name">Ovamir Capital</div>
      <div class="brand-slogan">Building Strength Through Capital</div>
    </div>
    <div class="contact-block">
      <p class="contact-line">555-555-0192<span class="divider">|</span>glenovamir@pvt.example</p>
      <p class="contact-line">1470 N Thornwick Rd, Suite 210<span class="divider">|</span>Marlow Falls, ST 00412</p>
    </div>
  </section>
</div>
</body>
</html>
```